Web Design Project

We need a web design company for a company based in London. We are an online minicab booking service that produces real time quotes on cab journey for consumers. Our colours are currently red and yellow, but do not need to stay that way; it's open to interpretation. Please avoid yellow and black as a colour combination. Our current site is: www.rovelto.co.uk We are looking for a new site to be user-friendly and easy to use, but more polished and professional looking, without using it usability and simplicity. We need to keep the booking capability on each page and it needs to draw in the user's eye. We need a site that is reliable and easy to use, but also fun.

Main objective: keep it simple, like it is now, but polish it up some. Also, we need to be able to add more content to it. And, we will also be adding a login capability for return users.

Target Market(s)

Internet-savvy people aged 18 and older.

Industry/Entity Type

It Company

Requirements
Must have
• Must have the booking widget. However, it doesn't have to be as large as it is now. We are actually thinking to split it over two pages. We will add a few options to the booking widget, such as another via option. The booking widget must be the most noticeable feature on the page. Sans serif font, please.
Should not have
• Should not be too busy and distracting. Please do not use any images of traditional taxis, ie. black cabs from London or yellow cabs from NYC. Our cars do not resemble these and our business cannot be associated with these images.

```html
<!DOCTYPE html>
<html lang="en">
<head>
<meta charset="utf-8">
<title>Rovelto – Online Cab Booking</title>
<link href="https://fonts.googleapis.com/css2?family=PT+Sans:wght@400;700&family=Crimson+Text:wght@700&display=swap" rel="stylesheet">
<style>
:root{
  --red:#d0080f;
  --red-dark:#a70009;
  --red-deep:#8e0006;
  --white:#ffffff;
  --panel:#f6f6f6;
  --border:#cfcfcf;
  --text:#6b6b6b;
  --label:#3a3a3a;
  --blue-top:#5fcbeb;
  --blue-bottom:#1d9fd2;
  --find:#27a6e6;
  --orange-top:#e35a1c;
  --orange-bottom:#b92a08;
  --accent:#e0201a;
  --footer:#f1f1f1;
}
*{box-sizing:border-box;margin:0;padding:0}
html,body{width:1200px;height:1167px;overflow:hidden}
body{position:relative;font-family:"PT Sans",Arial,sans-serif;background:var(--white);color:var(--text)}
.abs{position:absolute}
.header-band{left:0;top:0;width:1200px;height:516px;background:linear-gradient(180deg,var(--red) 0%,#c8050c 70%,#be030a 100%)}
.header-band::before{content:"";position:absolute;left:0;top:0;width:100%;height:9px;background:var(--red-deep)}
.order-now{left:692px;top:16px;color:var(--white);font-size:19px;letter-spacing:.3px}
.order-now b{font-weight:700}
.call-box{left:881px;top:0;width:283px;height:49px;background:var(--red-dark);border-radius:0 0 8px 8px;color:var(--white);font-size:22px;display:flex;align-items:center;justify-content:center;gap:10px;letter-spacing:.5px}
.call-box b{font-size:23px}
.brand{left:30px;top:86px;color:var(--white);font-size:56px;font-weight:700;line-height:1;display:flex;align-items:center;gap:12px}
.brand-mark{width:30px;height:30px;background:var(--white);border-radius:50%}
.main-nav{left:500px;top:101px;width:670px;height:55px;background:linear-gradient(180deg,#c40810,#b0040b);border:1px solid #e2343a;border-radius:8px;display:flex;box-shadow:inset 0 1px 0 rgba(255,255,255,.15)}
.main-nav a{color:#f5dede;text-decoration:none;font-size:19px;display:flex;align-items:center;justify-content:center;border-right:1px solid #8f0006;box-shadow:1px 0 0 #d9343a}
.main-nav a:last-child{border-right:0;box-shadow:none}
.main-nav a.current{color:var(--white)}
.hero-panel{left:20px;top:187px;width:1164px;height:442px;background:var(--panel);border:1px solid var(--border);border-radius:10px;box-shadow:0 6px 10px rgba(0,0,0,.12)}
.hero-photo{left:30px;top:198px;width:735px;height:420px;border-radius:8px;background:linear-gradient(160deg,#a9aeb2 0%,#7d8387 45%,#e3c22a 62%,#c89f16 72%,#54585b 100%);border:2px solid #d3d3d3}
.booking-head{left:775px;top:193px;width:401px;height:60px;background:linear-gradient(180deg,#ffffff,#ececec);border-radius:8px;display:flex;align-items:center;padding-left:24px;gap:14px}
.booking-head h2{font-family:"Crimson Text",Georgia,serif;color:var(--red);font-size:33px;font-weight:700}
.field-label{color:var(--label);font-size:14px}
.text-input{background:var(--white);border:1px solid #b9b9b9;height:31px;font-size:13px;font-style:italic;color:#8a8a8a;padding-left:10px;display:flex;align-items:center}
.find-btn{background:var(--find);color:var(--white);font-size:21px;height:33px;display:flex;align-items:center;justify-content:center}
.via-note{left:792px;top:320px;font-size:11px;font-style:italic;color:#9a9a9a;display:flex;align-items:center;gap:5px}
.via-note span{width:10px;height:10px;background:#c5c5c5}
.pax-row{left:789px;top:494px;display:flex;align-items:center;gap:8px;font-size:14px;color:var(--label)}
.pax-select{width:44px;height:20px;border:1px solid #9e9e9e;background:var(--white);font-size:11px;display:flex;align-items:center;justify-content:space-between;padding:0 5px;color:#666}
.quote-btn{left:796px;top:554px;width:364px;height:44px;border-radius:9px;background:linear-gradient(180deg,var(--orange-top),var(--orange-bottom));color:var(--white);font-size:19px;display:flex;align-items:center;justify-content:center}
.info-col{top:664px;height:370px;background:linear-gradient(180deg,#ffffff 0%,#ffffff 60%,#ececec 100%);border-right:1px solid #dcdcdc}
.info-col h3{height:61px;background:linear-gradient(180deg,var(--blue-top),var(--blue-bottom));color:var(--white);font-weight:400;font-size:23px;display:flex;align-items:center;padding-left:23px}
.info-col p{font-size:14px;line-height:20px;padding:0 22px 0 23px}
.steps{list-style:none;padding-left:25px;margin-top:18px}
.steps li{display:flex;align-items:center;gap:11px;height:29px;font-size:13.5px}
.steps b{color:var(--accent);font-size:18px;font-weight:400}
.steps a{color:var(--accent)}
.reason{padding:22px 22px 12px 24px;border-bottom:1px solid #e3e3e3}
.reason h4{color:var(--accent);font-weight:400;font-size:19px;line-height:22px}
.reason p{padding:0;font-size:14px}
.reason:last-child{border-bottom:0}
.site-footer{left:0;top:1061px;width:1200px;height:106px;background:var(--footer);border-top:1px solid #d4d4d4}
.footer-nav{left:22px;top:1081px;font-size:14px;color:#4a4a4a;display:flex;gap:15px}
.footer-nav i{font-style:normal;color:#777}
.touch{left:990px;top:1081px;font-size:14px;color:#4a4a4a;display:flex;align-items:center;gap:6px}
.social-square{width:22px;height:22px;background:#3b8ed0;border-radius:3px}
.copyright{left:902px;top:1127px;font-size:13px;color:#4a4a4a}
</style>
</head>
<body>
<div class="abs header-band"></div>
<div class="abs order-now">ONLINE <b>ORDER NOW</b></div>
<div class="abs call-box">CALL US <b>020 7946 0321</b></div>
<div class="abs brand"><span class="brand-mark"></span>Rovelto.co.uk</div>
<nav class="abs main-nav">
  <a class="current" href="#" style="width:117px">Home</a>
  <a href="#" style="width:166px">Rovelto Miles</a>
  <a href="#" style="width:116px">Join Us</a>
  <a href="#" style="width:127px">About Us</a>
  <a href="#" style="width:144px">Contact</a>
</nav>

<div class="abs hero-panel"></div>
<div class="abs hero-photo" role="img" aria-label="Photograph of a modern passenger van parked on a city street"></div>

<div class="abs booking-head">
  <h2>Book a Cab</h2>
  <svg width="34" height="24" viewBox="0 0 34 24" aria-hidden="true"><path d="M4 11 L8 3 H26 L30 11 H33 V19 H1 V11 Z" fill="#d0080f"/><rect x="10" y="5" width="14" height="6" fill="#fff"/><circle cx="8" cy="20" r="3.5" fill="#d0080f" stroke="#fff" stroke-width="1.5"/><circle cx="26" cy="20" r="3.5" fill="#d0080f" stroke="#fff" stroke-width="1.5"/></svg>
</div>

<div class="abs field-label" style="left:793px;top:264px">Pick me from:</div>
<div class="abs text-input" style="left:790px;top:286px;width:283px">type your destination here..</div>
<div class="abs find-btn" style="left:1078px;top:285px;width:81px">Find</div>
<div class="abs via-note"><span></span>add via address</div>

<div class="abs field-label" style="left:791px;top:352px">Pick me from:</div>
<div class="abs text-input" style="left:789px;top:373px;width:280px">type your destination here..</div>
<div class="abs find-btn" style="left:1076px;top:372px;width:81px">Find</div>

<div class="abs field-label" style="left:791px;top:418px">Pick me from:</div>
<div class="abs text-input" style="left:788px;top:440px;width:342px">06-Apr-2012 @ 5:32</div>

<div class="abs pax-row">Passengers <span class="pax-select">1 <small>&#8964;</small></span> Adults <span class="pax-select">1 <small>&#8964;</small></span> Bags</div>

<div class="abs quote-btn">Get Your no Obligation Quotes</div>

<section class="abs info-col" style="left:16px;width:386px">
  <h3>As Easy as Opening the Cab’s door</h3>
  <p style="margin-top:22px">Brightpath Studio is a web service company, offering a wide range of services which range from designing and development, that is covering almost all the fields in the best possible way.</p>
  <ol class="steps">
    <li><b>1</b><a href="#">Enter Your route</a></li>
    <li><b>2</b><a href="#">Quickly compare taxi fares</a></li>
    <li><b>3</b><a href="#">Get your travel confirmed on your phone by SMS</a></li>
  </ol>
</section>

<section class="abs info-col" style="left:404px;width:393px">
  <h3>Why Rovelto?</h3>
  <div class="reason"><h4>Price</h4><p>Brightpath Studio is a web service company, offering a wide range of services which range from designing</p></div>
  <div class="reason"><h4>No Fees</h4><p>Brightpath Studio is a web service company,</p></div>
  <div class="reason"><h4>Coverage</h4><p>Over years we have built a strong reputation in providing website design and web development services.</p></div>
</section>

<section class="abs info-col" style="left:799px;width:385px;border-right:0">
  <h3>Best Stories from our Community</h3>
  <p style="margin-top:22px">Brightpath Studio is a web service company, offering a wide range of services which range from designing and development, that is covering almost all the fields in the best possible way.</p>
  <p style="margin-top:8px">To be the best we know what and how to present beautifully the working of the client’s need and their advantages be highlighted. We act in accordance with the Industry certified processes to deliver the best to our clients all over the world. Over years we have built a strong reputation in providing website design and web development services.</p>
</section>

<footer class="abs site-footer"></footer>
<div class="abs footer-nav">Home <i>|</i> Rovelto Miles <i>|</i> Join Us <i>|</i> About Us <i>|</i> Contact</div>
<div class="abs touch">Get in Touch&nbsp;&nbsp;<span class="social-square"></span><span class="social-square"></span><span class="social-square"></span></div>
<div class="abs copyright">© 2012 Company Name &nbsp;|&nbsp; All right reserved</div>
</body>
</html>
```